Corporate Business Card

Very professional, Modern, Not to busy, include phone address email, website
(253) 555-0174, 61807 19th Street N, Kent, WA 98517, marcus@kestrelbayholding.com, brelvanindustries.com

Target Market(s)

Manufacturing

Industry/Entity Type

Aero, machining, manufacturing, Off road racing

Contact Information for Business Card

Phone, address email, website

```html
<!DOCTYPE html>
<html lang="en">
<head>
<meta charset="UTF-8">
<title>Brelvan Industries – Business Card</title>
<link href="https://fonts.googleapis.com/css2?family=Montserrat:wght@400;500;700;800&display=swap" rel="stylesheet">
<style>
  :root {
    --navy: #17336b;
    --red: #d1232b;
    --white: #ffffff;
    --backdrop: #3a3a3a;
    --divider: rgba(255,255,255,0.45);
  }
  * { box-sizing: border-box; margin: 0; padding: 0; }
  html, body { width: 1200px; height: 1200px; overflow: hidden; }
  body {
    background: var(--backdrop);
    font-family: "Montserrat", sans-serif;
    position: relative;
  }
  .card {
    position: absolute;
    left: 180px;
    width: 840px;
    height: 480px;
    border-radius: 34px;
    overflow: hidden;
    box-shadow: 0 18px 40px rgba(0,0,0,0.45);
  }
  .card-front { top: 90px; background: var(--white); }
  .card-back { top: 630px; background: var(--navy); }

  .front-top {
    position: absolute; left: 0; top: 0; width: 100%; height: 215px;
    display: flex; align-items: center; justify-content: center;
  }
  .brand-name {
    font-weight: 800;
    color: var(--navy);
    font-size: 54px;
    letter-spacing: 1px;
  }
  .accent-stripe {
    position: absolute; left: 0; top: 226px; width: 100%; height: 7px;
    background: var(--red);
  }
  .front-bottom {
    position: absolute; left: 0; top: 244px; width: 100%; height: 236px;
    background: var(--navy);
  }
  .identity {
    position: absolute; left: 70px; top: 70px;
    padding-left: 24px;
    border-left: 6px solid var(--red);
  }
  .person-name {
    color: var(--red); font-weight: 500; font-size: 40px; line-height: 1.05; letter-spacing: 1px;
  }
  .person-role {
    color: var(--white); font-weight: 400; font-size: 22px; margin-top: 6px; letter-spacing: 0.5px;
  }
  .vertical-divider {
    position: absolute; left: 400px; top: 38px; width: 1px; height: 160px;
    background: var(--divider);
  }
  .contact-list {
    position: absolute; left: 438px; top: 38px;
    list-style: none;
  }
  .contact-list li {
    display: flex; align-items: flex-start; gap: 14px;
    color: var(--white); font-size: 17px; line-height: 1.3;
    margin-bottom: 9px;
  }
  .contact-list svg { width: 20px; height: 20px; flex: none; margin-top: 1px; fill: var(--red); }

  .back-brand {
    position: absolute; inset: 0;
    display: flex; align-items: center; justify-content: center;
  }
  .back-brand .brand-name { color: var(--white); font-size: 70px; }
</style>
</head>
<body>

<section class="card card-front">
  <div class="front-top">
    <span class="brand-name">Brelvan Industries</span>
  </div>
  <div class="accent-stripe"></div>
  <div class="front-bottom">
    <div class="identity">
      <div class="person-name">JOHN DOE</div>
      <div class="person-role">CEO | FOUNDER</div>
    </div>
    <div class="vertical-divider"></div>
    <ul class="contact-list">
      <li>
        <svg viewBox="0 0 24 24" aria-hidden="true"><path d="M6.6 10.8a15.1 15.1 0 0 0 6.6 6.6l2.2-2.2c.3-.3.7-.4 1-.2 1.1.4 2.3.6 3.6.6.6 0 1 .4 1 1V20c0 .6-.4 1-1 1A17 17 0 0 1 3 4c0-.6.4-1 1-1h3.5c.6 0 1 .4 1 1 0 1.2.2 2.4.6 3.6.1.3 0 .7-.2 1z"/></svg>
        (253) 555-0174
      </li>
      <li>
        <svg viewBox="0 0 24 24" aria-hidden="true"><path d="M12 2a10 10 0 1 0 0 20 10 10 0 0 0 0-20zm6.9 6h-3a15.6 15.6 0 0 0-1.4-3.6A8 8 0 0 1 18.9 8zM12 4c.8 1.2 1.5 2.5 1.9 4h-3.8c.4-1.5 1.1-2.8 1.9-4zM4.3 14a8.2 8.2 0 0 1 0-4h3.4a16.5 16.5 0 0 0 0 4zm.8 2h3a15.6 15.6 0 0 0 1.4 3.6A8 8 0 0 1 5.1 16zm3-8h-3a8 8 0 0 1 4.4-3.6C8.9 5.5 8.4 6.7 8.1 8zM12 20c-.8-1.2-1.5-2.5-1.9-4h3.8c-.4 1.5-1.1 2.8-1.9 4zm2.3-6H9.7a14.7 14.7 0 0 1 0-4h4.6a14.7 14.7 0 0 1 0 4zm.2 5.6c.6-1.1 1.1-2.3 1.4-3.6h3a8 8 0 0 1-4.4 3.6zm1.8-5.6a16.5 16.5 0 0 0 0-4h3.4a8.2 8.2 0 0 1 0 4z"/></svg>
        brelvanindustries.com
      </li>
      <li>
        <svg viewBox="0 0 24 24" aria-hidden="true"><path d="M12 2a7 7 0 0 0-7 7c0 5.2 7 13 7 13s7-7.8 7-13a7 7 0 0 0-7-7zm0 9.5A2.5 2.5 0 1 1 12 6.5a2.5 2.5 0 0 1 0 5z"/></svg>
        <span>61807 19th Street N<br>Kent, WA 98517</span>
      </li>
      <li>
        <svg viewBox="0 0 24 24" aria-hidden="true"><path d="M2 5h20v14H2zm2 2v.5l8 5 8-5V7zm0 2.8V17h16V9.8l-8 5z"/></svg>
        marcus@kestrelbayholding.com
      </li>
    </ul>
  </div>
</section>

<section class="card card-back">
  <div class="back-brand">
    <span class="brand-name">Brelvan Industries</span>
  </div>
</section>

</body>
</html>
```